TRU PEAK POWER.

I'd like my business logo.
contact name: Desmond Halvik
phone:0438275160
email: info@trupeakpower.net.au
website: www.trupeakpower.net.au

services:
solar
battery storage
LED lighting
energy saving solutions
general electrical
I'd like the design to look professional

Target Market(s)

Everyone

Industry/Entity Type

Business

Contact Information for Business Card

as described above

Requirements
Must have
• Id like the colours and the design to work well with my logo.

```html
<!DOCTYPE html>
<html lang="en">
<head>
<meta charset="UTF-8">
<title>Tru Peak Power – Business Card</title>
<link rel="stylesheet" href="https://fonts.googleapis.com/css2?family=Open+Sans:wght@400;600;700&display=swap">
<style>
  :root {
    --backdrop: #4a4a4a;
    --card-white: #ffffff;
    --green: #4ea232;
    --green-light: #93c73a;
    --orange: #f7941d;
    --orange-light: #fbb314;
    --orange-deep: #f4861e;
    --text-grey: #555555;
    --divider: #c9c9c9;
  }
  * { box-sizing: border-box; margin: 0; padding: 0; }
  html, body {
    width: 1105px;
    height: 1200px;
    overflow: hidden;
  }
  body {
    background: var(--backdrop);
    font-family: "Open Sans", Arial, sans-serif;
    position: relative;
  }
  .card {
    position: absolute;
    left: 193px;
    width: 718px;
    height: 409px;
    overflow: hidden;
    box-shadow: 0 4px 10px rgba(0,0,0,0.45);
  }
  .card--front { top: 168px; background: var(--card-white); }
  .card--back {
    top: 624px;
    background: radial-gradient(ellipse at 50% 35%, var(--orange-light) 0%, var(--orange) 60%, var(--orange-deep) 100%);
  }

  /* Front */
  .brand {
    position: absolute;
    display: flex;
    align-items: center;
    gap: 12px;
    font-weight: 700;
    white-space: nowrap;
  }
  .brand__dot {
    border-radius: 50%;
    flex: none;
  }
  .card--front .brand {
    left: 50px;
    top: 186px;
    font-size: 27px;
    color: var(--green);
    letter-spacing: 0.5px;
  }
  .card--front .brand__dot {
    width: 34px; height: 34px;
    background: var(--orange);
  }
  .divider {
    position: absolute;
    left: 365px;
    top: 133px;
    width: 1px;
    height: 138px;
    background: var(--divider);
  }
  .contact {
    position: absolute;
    left: 388px;
    top: 138px;
  }
  .contact__name {
    font-size: 25px;
    font-weight: 600;
    color: var(--green);
    line-height: 34px;
    margin-bottom: 6px;
  }
  .contact__row {
    display: flex;
    align-items: center;
    gap: 9px;
    font-size: 18px;
    color: var(--text-grey);
    line-height: 27.5px;
  }
  .contact__icon { width: 17px; height: 17px; flex: none; }
  .accent-band {
    position: absolute;
    left: 0;
    bottom: 0;
    width: 718px;
    height: 28px;
  }

  /* Back */
  .card--back .brand {
    left: 0;
    right: 0;
    justify-content: center;
    top: 158px;
    font-size: 48px;
    color: var(--card-white);
    letter-spacing: 1px;
  }
  .card--back .brand__dot {
    width: 54px; height: 54px;
    background: var(--card-white);
  }
  .services {
    position: absolute;
    left: 0;
    right: 0;
    top: 314px;
    text-align: center;
    color: var(--card-white);
    font-size: 19px;
    line-height: 27.5px;
  }
  .services__sep { margin: 0 6px; }
</style>
</head>
<body>

<section class="card card--front" aria-label="Business card front">
  <div class="brand">
    <span class="brand__dot"></span>
    <span class="brand__name">TRU PEAK POWER</span>
  </div>

  <div class="divider"></div>

  <div class="contact">
    <p class="contact__name">Desmond Halvik</p>
    <p class="contact__row">
      <svg class="contact__icon" viewBox="0 0 24 24" aria-hidden="true">
        <path fill="#4ea232" d="M6.6 10.8a15.1 15.1 0 0 0 6.6 6.6l2.2-2.2a1 1 0 0 1 1-.25 11.4 11.4 0 0 0 3.6.57 1 1 0 0 1 1 1V20a1 1 0 0 1-1 1A17 17 0 0 1 3 4a1 1 0 0 1 1-1h3.5a1 1 0 0 1 1 1c0 1.25.2 2.45.57 3.6a1 1 0 0 1-.25 1z"/>
      </svg>
      <span>0438275160</span>
    </p>
    <p class="contact__row">
      <svg class="contact__icon" viewBox="0 0 24 24" aria-hidden="true">
        <rect x="2" y="5" width="20" height="14" rx="1.5" fill="#4ea232"/>
        <path d="M3 6.5l9 6.5 9-6.5" fill="none" stroke="#ffffff" stroke-width="1.6"/>
      </svg>
      <span>info@trupeakpower.net.au</span>
    </p>
    <p class="contact__row">
      <svg class="contact__icon" viewBox="0 0 24 24" aria-hidden="true">
        <circle cx="12" cy="12" r="10" fill="#4ea232"/>
        <path d="M2.5 12h19M12 2.2c3 3 3 16.6 0 19.6M12 2.2c-3 3-3 16.6 0 19.6" fill="none" stroke="#ffffff" stroke-width="1.3"/>
      </svg>
      <span>www.trupeakpower.net.au</span>
    </p>
  </div>

  <svg class="accent-band" viewBox="0 0 718 28" preserveAspectRatio="none" aria-hidden="true">
    <defs>
      <linearGradient id="band-green" x1="0" x2="1" y1="0" y2="0">
        <stop offset="0" stop-color="#4ea232"/>
        <stop offset="0.5" stop-color="#93c73a"/>
        <stop offset="1" stop-color="#4ea232"/>
      </linearGradient>
      <linearGradient id="band-orange" x1="0" x2="1" y1="0" y2="0">
        <stop offset="0" stop-color="#f4861e"/>
        <stop offset="1" stop-color="#fbb314"/>
      </linearGradient>
    </defs>
    <polygon points="0,0 467,0 458,28 0,28" fill="url(#band-green)"/>
    <polygon points="474,0 718,0 718,28 465,28" fill="url(#band-orange)"/>
  </svg>
</section>

<section class="card card--back" aria-label="Business card back">
  <div class="brand">
    <span class="brand__dot"></span>
    <span class="brand__name">TRU PEAK POWER</span>
  </div>
  <div class="services">
    <p>Solar<span class="services__sep">•</span>Battery storage<span class="services__sep">•</span>LED lighting</p>
    <p>Energy saving solutions</p>
  </div>
</section>

</body>
</html>
```